Webdesign/ Redesign of community frontpage (only design, no code!)

Our social community website (http://www.tavoro.eu) needs a fresh, more invitating frontpage. Our audience are 14 - 25 year old.

Only the screen design (psd & image) is needed, no code (no html, no css, ...).

Style:
- Modern/ clear/ lightweight/ invitating design for young people
- Emphasize the intent of the website (social community website, meeting other young people to chat, hangout, ..)
- Optimized for 1024x768

Elements that must appear:
- Logo (attached as EPS, can be modified if needed)
- Login form (Username, Password, Status/Feeling, Forgot password link, ...)
- Link to registration page OR registration form
- Empty space (around 350x250 pixel) where a video or other dynamic content could be embedded (done by myself)
- Five feature/pro statements (max. 60 letters each, not necessarily to be displayed as a group, see below)
- Currently present links in footer
- Some statistics (Number of people online, total number of members (females/ males))

Elements that might appear:
- Registration form instead of link to separate registration form (ex like chatterbox has it)

Ideas:
- Registration form could also be designed to be a layer that'll show when the user clicks
- If the design needs/allows it, I can also animate random member photos (80x80 pixels) and place them on the frontpage using js/ ajax

Feature/pro statements examples (see above):
- Dauerhaft kostenlos für Frauen und Männer
- Reale Profile, extrem wenig Fakes & Störenfriede
- Persönliches Profil mit vielen Funktionen
- Hoher Schutz deiner Privatsphäre und Daten
- Viele freundliche Mitarbeiter und Helfer
Updates

After having reviewed the first two designs, I'd like to give these general ideas/ feedback:

1. I think it would be much better to _not_ have the whole registration form on the frontpage but instead only a link which opens the form in a layer/dialog when clicked. Of course only the design of the dialog needs to be done, I'll do the actual coding. To have a first impression of how the dialog could look like, please see the newly attached dialog.png (the text in the dialog is just for demo and should be replaced by the actual registration form).

2. There should be no separation between males/ females like it is currently. I think it'd better to mix because it emphasizes the community/ group character of the site and does not make it look too much like da dating site.

3. I think the five statements/ pros I mentioned (why should people register, what are the greatest features of our site, ..) could be best displayed as balloon tips (just like in comics) next to some images of users.

4. The color of the site should not be too heavy and should make people feel comfortable.

5. The logo provied must be fixed to read "TAVORO.eu" instead of "LUNEPA.de". I hope this i no big deal, sorry for that. This could also be done afterwards for a small additional amount of money, as it doesn't really affect the overall design.

To better illustrate all my writings above I just made two simple sketches and attached them (frontpage.png and frontpage_with_active_registration.png).

Important: these only show all the elements that must appear on the page and what I thought might be a good idea of how to present the pros/ features of my site. The actual placements, sizes, arragements etc. can of course all be different.

Looking forward to your create additions and design skills to make this look pretty... :-)

Just to emphasize, the design should not look or feel heavy. So please keep the colors light/ soft, no huge images, don't stretch the logo to much, etc.

Please do not insert any content (like search boxes, text blocks, etc.) which is not already present in my mockups. The only thing that should be additionally added is a link/ button so people can login using keypass (chatterbox, searchly, ..) too.

Target Market(s)

Young people 14 - 25 years old interested in meeting friends, new people, chat, flirt, hangout, have fun.

Industry/Entity Type

Community

Requirements
Must have
• see description
Nice to have
• see description
Should not have
• plugin dependencies (ex flash)

```html
<!DOCTYPE html>
<html lang="de">
<head>
<meta charset="utf-8">
<title>TAVORO.eu – Registrierung</title>
<link rel="stylesheet" href="https://fonts.googleapis.com/css2?family=Arimo:wght@400;700&family=Roboto+Condensed:wght@700&display=swap">
<style>
  :root {
    --header-top: #8a2329;
    --header-bottom: #5b1519;
    --strip: #7a1e23;
    --page-bg: #efe4d4;
    --footer: #55181b;
    --wine: #6e1a20;
    --ribbon: #a3262d;
    --orange: #e9a14c;
    --yellow: #f2c13a;
    --ink: #1b1b1b;
    --field-border: #a8a8a8;
    --avatar: #c9c9c9;
    --avatar-frame: #ffffff;
    --bubble-top: #ececec;
    --bubble-bottom: #bdbdbd;
    --photo-a: #d8c7c2;
    --photo-b: #8c6a66;
  }
  * { box-sizing: border-box; margin: 0; padding: 0; }
  html, body { width: 1200px; height: 900px; overflow: hidden; }
  body {
    position: relative;
    font-family: "Arimo", Arial, sans-serif;
    background: var(--page-bg);
    color: var(--ink);
  }
  .abs { position: absolute; }

  /* Header */
  .header {
    left: 0; top: 0; width: 1200px; height: 344px;
    background: linear-gradient(180deg, var(--header-top), var(--header-bottom));
  }
  .header-photos {
    left: 680px; top: 80px; width: 520px; height: 252px;
    background: linear-gradient(120deg, var(--photo-b), var(--photo-a) 55%, var(--photo-b));
  }
  .brand-name {
    left: 104px; top: 14px; color: #fff; font-weight: 700; font-size: 64px; letter-spacing: 1px;
  }
  .brand-tagline {
    left: 104px; top: 96px; color: #fff; font-weight: 700; font-size: 34px;
  }
  .signup-title {
    left: 100px; top: 180px; color: #fff;
    font-family: "Roboto Condensed", Arial, sans-serif; font-size: 48px;
  }
  .signup-sub { left: 100px; top: 234px; color: var(--orange); font-size: 26px; }
  .signup-button {
    left: 244px; top: 278px; width: 110px; height: 36px; border-radius: 18px;
    background: linear-gradient(#e4e4e4, #a9a9a9); color: #333; font-weight: 700; font-size: 18px;
    line-height: 36px; padding-left: 16px;
  }

  /* Login */
  .login-field {
    top: 24px; height: 22px; background: #fff; border: 1px solid #ccc;
    font-size: 13px; line-height: 20px; padding-left: 6px; color: #222;
  }
  .login-user { left: 578px; width: 160px; }
  .login-pass { left: 744px; width: 160px; }
  .login-status { left: 912px; width: 164px; }
  .login-status svg { position: absolute; right: 6px; top: 5px; }
  .remember { left: 580px; top: 50px; color: #fff; font-size: 12px; display: flex; align-items: center; gap: 6px; }
  .remember span.box { width: 10px; height: 10px; background: #fff; }
  .forgot { left: 748px; top: 50px; color: var(--yellow); font-size: 13px; text-decoration: underline; }

  /* Strip */
  .strip {
    left: 0; top: 344px; width: 1200px; height: 54px; background: var(--strip);
    color: #fff; font-weight: 700; font-size: 22px; text-align: center; line-height: 54px;
  }

  /* Members & bubbles */
  .avatar { background: var(--avatar); border: 4px solid var(--avatar-frame); }
  .bubble {
    background: linear-gradient(var(--bubble-top), var(--bubble-bottom));
    border: 3px solid #555; border-radius: 16px; font-weight: 700; color: #111;
    display: flex; align-items: center; justify-content: center;
  }
  .bubble-lol { left: 70px; top: 516px; width: 100px; height: 54px; font-size: 18px; }
  .bubble-love { left: 70px; top: 660px; width: 182px; height: 96px; font-size: 24px; border-radius: 24px; }

  /* Side panels */
  .panel { background: rgba(255,255,255,0.35); border: 2px solid #e2d4c2; }
  .ribbon {
    background: linear-gradient(var(--ribbon), var(--wine)); color: #fff; font-weight: 700;
    font-size: 24px; text-align: center;
  }
  .stat { color: #222; font-size: 12px; font-weight: 700; }
  .pros { right: 24px; top: 676px; width: 360px; text-align: right; font-size: 13px; line-height: 22px; font-weight: 700; color: #333; }
  .pros .cta { color: var(--ribbon); }

  /* Footer */
  .footer {
    left: 0; top: 870px; width: 1200px; height: 30px; background: var(--footer);
    color: #fff; font-size: 12px; text-align: center; line-height: 30px;
  }

  /* Registration dialog */
  .dialog {
    left: 296px; top: 136px; width: 612px; height: 676px;
    background: #fff; border: 6px solid #111; border-radius: 30px;
  }
  .dialog-close {
    left: 852px; top: 100px; width: 70px; height: 76px; background: #111;
    border-radius: 8px; box-shadow: inset 0 0 0 4px #111, inset 0 0 0 7px #ddd;
  }
  .dialog-close svg { position: absolute; left: 20px; top: 23px; }
  .section-title { left: 346px; color: var(--wine); font-weight: 700; font-size: 22px; }
  .form-label { left: 346px; font-size: 16px; font-weight: 700; color: #111; }
  .form-field {
    left: 560px; width: 180px; height: 16px; border: 1px solid var(--field-border); background: #f7f7f7;
  }
  .option { left: 568px; font-size: 15px; font-weight: 700; display: flex; align-items: center; gap: 8px; }
  .option span.dot { width: 9px; height: 9px; border-radius: 50%; background: #222; }
  .terms-title { left: 346px; top: 658px; font-size: 21px; font-weight: 700; color: var(--wine); }
  .terms-check { left: 348px; top: 686px; width: 300px; font-size: 15px; font-weight: 700; line-height: 18px; display: flex; gap: 6px; }
  .terms-check span.dot { flex: none; margin-top: 4px; width: 9px; height: 9px; border-radius: 50%; background: #222; }
  .submit {
    left: 524px; top: 744px; width: 176px; height: 32px; border-radius: 16px;
    background: linear-gradient(#a42a30, var(--wine)); color: #fff; font-weight: 700; font-size: 16px;
    text-align: center; line-height: 32px;
  }
</style>
</head>
<body>

<div class="abs header"></div>
<div class="abs header-photos" role="img" aria-label="Collage of member photos"></div>

<div class="abs brand-name">TAVORO.eu</div>
<div class="abs brand-tagline">chat, flirt &amp; more</div>

<div class="abs login-field login-user">Username</div>
<div class="abs login-field login-pass">Password</div>
<div class="abs login-field login-status">Status/Feeling
  <svg width="12" height="10" viewBox="0 0 12 10"><path d="M0 0h12L6 10z" fill="#111"/></svg>
</div>
<div class="abs remember"><span class="box"></span>Remember me</div>
<div class="abs forgot">Forgot Password?</div>

<div class="abs signup-title">NO ACCOUNT YET?</div>
<div class="abs signup-sub">Sign Up - it's free and easy to be!</div>
<div class="abs signup-button">Sign Up</div>

<div class="abs strip">Chatten, Flirten, nette Leute kennenlernen – deine Internet Community!</div>

<!-- Members with speech bubbles -->
<div class="abs avatar" style="left:56px;top:412px;width:96px;height:100px" role="img" aria-label="Member photo"></div>
<div class="abs avatar" style="left:158px;top:584px;width:94px;height:98px" role="img" aria-label="Member photo"></div>
<div class="abs avatar" style="left:56px;top:746px;width:96px;height:96px" role="img" aria-label="Member photo"></div>
<div class="abs bubble bubble-lol">LOL!</div>
<div class="abs bubble bubble-love">I love it..!</div>

<!-- Recently online -->
<div class="abs panel" style="left:808px;top:412px;width:372px;height:206px"></div>
<div class="abs ribbon" style="left:808px;top:412px;width:372px;height:40px;line-height:40px">Zuletzt eingeloggt</div>
<div class="abs avatar" style="left:822px;top:464px;width:96px;height:106px" role="img" aria-label="Member photo"></div>
<div class="abs avatar" style="left:926px;top:464px;width:92px;height:106px" role="img" aria-label="Member photo"></div>
<div class="abs avatar" style="left:1026px;top:464px;width:96px;height:106px" role="img" aria-label="Member photo"></div>
<div class="abs stat" style="left:910px;top:570px">XX.XXX&nbsp; Members</div>
<div class="abs stat" style="left:910px;top:586px">X.XXX&nbsp; New Online</div>

<!-- Why a free profile -->
<div class="abs panel" style="left:808px;top:626px;width:372px;height:238px"></div>
<div class="abs ribbon" style="left:808px;top:626px;width:372px;height:36px;line-height:36px;font-size:18px">Warum kostenloses Profil?</div>
<div class="abs pros">
  <div class="cta">Deine kostenlose Flirt Community!</div>
  <div>Dauerhaft kostenlos für Frauen und Männer</div>
  <div>Reale Profile, extrem wenig Fakes &amp; Störenfriede</div>
  <div>Persönliches Profil mit vielen Funktionen</div>
  <div>Hoher Schutz deiner Privatsphäre und Daten</div>
  <div>Viele freundliche Mitarbeiter und Helfer</div>
  <div class="cta">Sei dabei: jetzt kostenloses Profil erstellen.</div>
</div>

<div class="abs footer">Häufig gestellte Fragen | Nutzungsregeln | Jugendschutz | Datenschutz | Team &amp; Helfer | Kontakt</div>

<!-- Registration dialog -->
<div class="abs dialog"></div>
<div class="abs dialog-close">
  <svg width="30" height="30" viewBox="0 0 30 30"><path d="M3 3L27 27M27 3L3 27" stroke="#fff" stroke-width="6"/></svg>
</div>

<div class="abs section-title" style="top:152px">Persönliche Daten</div>
<div class="abs form-label" style="top:198px">Geschlecht</div>
<div class="abs form-field" style="top:200px"></div>
<div class="abs form-label" style="top:226px">Geburtsdatum</div>
<div class="abs form-field" style="top:228px"></div>
<div class="abs form-label" style="top:256px">Vorname</div>
<div class="abs form-field" style="top:258px"></div>
<div class="abs form-label" style="top:286px">Wohnort</div>
<div class="abs form-field" style="top:288px"></div>
<div class="abs form-label" style="top:314px">Interesse an</div>
<div class="abs option" style="top:314px"><span class="dot"></span>Freundschaftspflege</div>
<div class="abs option" style="top:334px"><span class="dot"></span>Sport-/ Freizeitpartner</div>
<div class="abs option" style="top:354px"><span class="dot"></span>Chat-/ eMail-Freundschaft</div>
<div class="abs option" style="top:374px"><span class="dot"></span>Flirten &amp; Daten</div>
<div class="abs option" style="top:394px"><span class="dot"></span>Feste Beziehung</div>

<div class="abs section-title" style="top:432px">Zugangsdaten</div>
<div class="abs form-label" style="top:480px">eMail-Adresse</div>
<div class="abs form-field" style="top:482px"></div>
<div class="abs form-label" style="top:520px">Benutzername</div>
<div class="abs form-field" style="top:522px"></div>
<div class="abs form-label" style="top:562px">Passwort</div>
<div class="abs form-field" style="top:564px"></div>
<div class="abs form-label" style="top:600px">Passwort erneut</div>
<div class="abs form-field" style="top:602px"></div>

<div class="abs terms-title">Allgemeinen Geschäfts- und Nutzungsbedingungen</div>
<div class="abs terms-check"><span class="dot"></span><span>Ich habe die Nutzungsbedingungen gelesen, verstanden und stimme diesen zu.</span></div>
<div class="abs submit">Profil Erstellen</div>

</body>
</html>
```